Disability Support service provider Needs a shopfront graphic Design

We are based in Sydney, Australia. Our company is called 'Bright Harbour Care Services'. We provide care services to anyone with a disability. I would like to see designs that are colourful and perhaps transparent. The colours from my logo uploaded can be used as a guide. I would also like a bit of information about our services on the design somewhere maybe in point form, for eg. Disability Support Services, We are people helping People, take control of your disability, supporting people to live the life they want to live, I would like the design to be friendly and inviting.

```html
<!DOCTYPE html>
<html lang="en">
<head>
<meta charset="utf-8">
<title>Bright Harbour Care Services – Shopfront Graphic</title>
<link rel="stylesheet" href="https://fonts.googleapis.com/css2?family=Cinzel:wght@600&family=Open+Sans:wght@400;700&display=swap">
<style>
  :root {
    --brand-blue: #6985bb;
    --panel-grey: #a9aaad;
    --frame-line: #e2e2e2;
    --leaf-green: #8fc63f;
    --white: #ffffff;
  }
  html, body {
    margin: 0;
    padding: 0;
    width: 1200px;
    height: 1200px;
    overflow: hidden;
    background: var(--white);
  }
  .shopfront {
    position: absolute;
    left: 40px;
    top: 273px;
    width: 1098px;
    height: 553px;
    font-family: "Open Sans", Arial, sans-serif;
  }
  .shopfront-bg {
    position: absolute;
    inset: 0;
  }
  .headline {
    position: absolute;
    left: 22px;
    top: 40px;
    margin: 0;
    font-family: "Cinzel", "Times New Roman", serif;
    font-weight: 600;
    font-size: 34px;
    line-height: 39px;
    color: var(--brand-blue);
    letter-spacing: 0.5px;
  }
  .intro {
    position: absolute;
    left: 22px;
    top: 139px;
    margin: 0;
    font-size: 22px;
    line-height: 30px;
    color: var(--white);
  }
  .service-list {
    position: absolute;
    left: 20px;
    top: 215px;
    margin: 0;
    padding: 0;
    list-style: none;
  }
  .service-list li {
    position: relative;
    padding-left: 22px;
    font-weight: 700;
    font-size: 23px;
    line-height: 28px;
    color: var(--white);
    letter-spacing: 0.2px;
  }
  .service-list li::before {
    content: "";
    position: absolute;
    left: 0;
    top: 10px;
    width: 11px;
    height: 8px;
    border-radius: 50%;
    background: var(--leaf-green);
  }
  .service-list li + li { margin-top: 11px; }
  .service-list li:nth-child(3) { margin-top: 18px; }
  .audience {
    position: absolute;
    left: 22px;
    top: 423px;
    margin: 0;
    font-size: 23px;
    line-height: 36px;
    color: var(--brand-blue);
  }
  .brand {
    position: absolute;
    left: 458px;
    top: 100px;
    width: 580px;
    text-align: center;
  }
  .brand-dot {
    display: block;
    width: 96px;
    height: 96px;
    margin: 0 auto 30px;
    border-radius: 50%;
    background: var(--white);
  }
  .brand-name {
    margin: 0;
    font-family: "Cinzel", "Times New Roman", serif;
    font-weight: 600;
    font-size: 40px;
    line-height: 44px;
    color: var(--white);
  }
  .contact {
    margin: 40px 0 0;
    color: var(--white);
    font-size: 20px;
    line-height: 28px;
  }
  .contact .phone { font-weight: 700; display: block; }
</style>
</head>
<body>
  <section class="shopfront">
    <svg class="shopfront-bg" width="1098" height="553" viewBox="0 0 1098 553">
      <rect x="0.5" y="0.5" width="1097" height="552" fill="#ffffff" stroke="#e2e2e2"/>
      <rect x="2" y="132" width="470" height="263" fill="#6985bb"/>
      <path d="M358,0 Q454,276.5 358,553 L1098,553 L1098,0 Z" fill="#a9aaad"/>
      <path d="M358,0 Q454,276.5 358,553" fill="none" stroke="#ffffff" stroke-width="3"/>
    </svg>

    <h1 class="headline">We are people<br>helping People</h1>

    <p class="intro">Supporting you to live the life<br>you want to live with</p>

    <ul class="service-list">
      <li>TRAVEL</li>
      <li>CLEANING</li>
      <li>ACCOMMODATION</li>
      <li>EVERYDAY HOUSEHOLD TASKS</li>
    </ul>

    <p class="audience">for the elderly and people<br>with a disability</p>

    <div class="brand">
      <span class="brand-dot"></span>
      <p class="brand-name">Bright Harbour<br>Care Services</p>
      <p class="contact">
        <span class="phone">1300 000 000</span>
        brightharbourcare.com.au
      </p>
    </div>
  </section>
</body>
</html>
```